Corporate Financial Services

This is a new Company. The ROW represents my son's and my own Christian name initials (ROW) (Colin and Brent) but no real significance.
This is a boutique financial services company active in the full parameter of corporate and business transactions. From standard financial and tax services to specialised Research & Development, mergers and acquisitions, business valuations, and capital raising.
Over 30 years of experience with listed and private entities.
I am after something exciting, given the nature of the business, bright, clean and colourful, but not in comic form.
Hi there,
Firstly thankyou for accepting the challenge. I have no ideas and nothing to compare your submissions with other than other peoples cards.
A few points
I omitted the ABN number from the card description. This is an important reference for all businesses operating in Australia. Therefore the following should be shown in association with the company name ROW Corporate & Financial Services Pty Ltd It can either be within brackets or without but always shown underneath the company name in smaller font.
The eight core business services need to be shown on the reverse
My contact number should also be shown along side the address
My business title is Chartered Accountant in full. I am also not fussed as to whether my name appears in caps or Caps and lowercase ie Brent Ashdown or BRENT ASHDOWN but this will depend upon the design of the rest of the card.
Maybe a small logo for the company needs to be attached but not sure.
Kind regards
Brent Ashdown
Financial
ROW Corporate & Financial Services Pty Ltd
(ABN 71 309 482 157)
(Note ABN could be shown on the reverse side with just ROW Corporate & Financial Services Pty Ltd on the front....no ABN
17 Wattlebank Street Norvale SA 5174
Brent Ashdown
Chartered Accountant
Phone (symbol preferred) +61 (0) 437 215604
Email (symbol) to be provided
www.rowfinsvc-example.com.au
Skype brent7312
- On the reverse:
Corporate Finance
Taxation
Research & Development Specialisation
Financial Accounting
Mergers & Acquisitions
Company Listings (IPO's)
Business Valuations
Capital Raising
- Interested in a strong black card (or grey white platinum and black colours) with either platinum or gold highlight modern name style no italics. I would also like at a later stage with the winner to use this same design for card for Asia with a red and or gold and platinum colour. But I want this batch first.
The smart block (square) for digital image transfer to mobile phones contained within a gold or platinum square border on reverse of the card
Anything old or staid looking. No italics sans serif

```html
<!DOCTYPE html>
<html lang="en">
<head>
<meta charset="utf-8">
<title>ROW Corporate &amp; Financial Services – Business Card</title>
<link href="https://fonts.googleapis.com/css2?family=Open+Sans:wght@300;400;600;700;800&display=swap" rel="stylesheet">
<style>
  :root{
    --backdrop:#d9d6d1;
    --card-black:#0c0c0c;
    --card-charcoal:#1e1e1e;
    --card-white:#ffffff;
    --ink:#151515;
    --gold-light:#e7cf97;
    --gold-mid:#b8924f;
    --gold-dark:#6b4f22;
    --watermark:#242424;
  }
  *{margin:0;padding:0;box-sizing:border-box;}
  html,body{width:1200px;height:912px;overflow:hidden;background:var(--backdrop);}
  body{font-family:"Open Sans",Arial,sans-serif;position:relative;}
  .business-card{
    position:absolute;left:100px;top:170px;width:1000px;height:572px;
    border-radius:6px;overflow:hidden;background:var(--card-black);
    box-shadow:0 14px 40px rgba(0,0,0,.25);
  }
  .card-shapes{position:absolute;inset:0;}
  .brand-watermark{
    position:absolute;right:-10px;bottom:40px;
    font-size:230px;font-weight:800;letter-spacing:-6px;line-height:1;
    color:var(--watermark);
  }
  .company-name{
    position:absolute;right:46px;top:78px;text-align:right;color:var(--ink);
    text-transform:uppercase;line-height:1.05;
  }
  .company-name .line-light{display:block;font-size:34px;font-weight:300;letter-spacing:.5px;}
  .company-name .line-bold{display:block;font-size:36px;font-weight:800;letter-spacing:-.5px;}
  .name-plate{
    position:absolute;left:120px;top:318px;width:470px;height:92px;
    border-radius:8px 46px 46px 8px;
    background:linear-gradient(90deg,var(--gold-dark) 0%,var(--gold-mid) 35%,var(--gold-light) 60%,var(--gold-mid) 85%,var(--gold-dark) 100%);
    padding:14px 0 0 130px;color:#fff;
  }
  .person-name{font-size:30px;font-weight:800;letter-spacing:.5px;line-height:1.1;}
  .person-title{font-size:19px;font-weight:400;line-height:1.3;}
  .address-line{
    position:absolute;left:48px;top:452px;color:#fff;font-size:24px;font-weight:400;
    display:flex;align-items:center;gap:14px;
  }
  .address-line .brand-dot{width:16px;height:16px;border-radius:50%;background:var(--gold-light);}
</style>
</head>
<body>
  <div class="business-card">
    <svg class="card-shapes" width="1000" height="572" viewBox="0 0 1000 572">
      <defs>
        <linearGradient id="sheen" x1="0" y1="0" x2="1" y2="0">
          <stop offset="0" stop-color="#0c0c0c"/>
          <stop offset=".6" stop-color="#1e1e1e"/>
          <stop offset="1" stop-color="#0c0c0c"/>
        </linearGradient>
      </defs>
      <rect width="1000" height="572" fill="url(#sheen)"/>
      <path class="white-band" fill="#ffffff"
        d="M0,150 C260,150 420,90 640,70 C800,56 900,52 1000,48
           L1000,250 C880,262 760,268 640,290 C520,312 430,340 330,336
           C220,332 120,300 0,300 Z"/>
      <path class="charcoal-swoosh" fill="#1a1a1a" opacity=".9"
        d="M0,300 C120,300 220,332 330,336 C430,340 520,312 640,290
           C760,268 880,262 1000,250 L1000,266 C880,280 760,286 640,306
           C520,328 430,356 330,352 C220,348 120,318 0,316 Z"/>
    </svg>
    <div class="brand-watermark" aria-hidden="true">ROW</div>
    <div class="company-name">
      <span class="line-light">ROW Corporate &amp;</span>
      <span class="line-bold">Financial Services</span>
    </div>
    <div class="name-plate">
      <div class="person-name">BRENT ASHDOWN</div>
      <div class="person-title">Chartered Accountant</div>
    </div>
    <div class="address-line">
      <span class="brand-dot"></span>
      <span>Pty Ltd 17 Wattlebank Street Norvale SA 5174</span>
    </div>
  </div>
</body>
</html>
```